Corporate Dinner Invite at Verolla for PMV

PMV is hosting a corporate dinner at the BRQ Conference and we need an email attachment invite for the event. Please use some images from this site for inspiration: https://www.verollaexample.com/fernparlor/

Invite Title:
Join us for dinner!

Event Details:
Tuesday, October 24th 2023 at 6:30pm
Verolla Chicago, Fern Parlor
347 W Harlow Ave, Chicago, IL 60622

Target Market(s)

Corporate Audience

Font styles to use
Script

Colors
0054AA
0677BA
7BADD7
CADEEF
E8F1F8

Requirements
Must have
• PMV logo, event date / time, event location details, photo(s) from Fern Parlor

```html
<!DOCTYPE html>
<html lang="en">
<head>
<meta charset="utf-8">
<title>PMV Corporate Dinner Invite</title>
<link rel="stylesheet" href="https://fonts.googleapis.com/css2?family=Cinzel:wght@400;700&family=Great+Vibes&display=swap">
<style>
  :root {
    --navy-deep: #0a1a45;
    --navy: #10275e;
    --navy-light: #1b3a78;
    --royal: #06338f;
    --frame: #0a3aa6;
    --label-blue: #3472e6;
    --script-blue: #3d7be8;
    --rule: #2c5b9c;
    --logo-blue: #1f63d8;
    --white: #ffffff;
  }
  * { margin: 0; padding: 0; box-sizing: border-box; }
  html, body { width: 1200px; height: 797px; overflow: hidden; background: var(--navy-deep); }
  .invite {
    position: relative;
    width: 1200px;
    height: 797px;
    overflow: hidden;
    background:
      radial-gradient(ellipse 420px 300px at 820px 20px, rgba(120,150,200,0.35), transparent 70%),
      linear-gradient(180deg, var(--navy) 0%, var(--navy-deep) 100%);
  }
  .venue-photo {
    position: absolute;
    left: 0; top: 0;
    width: 560px; height: 797px;
    background:
      radial-gradient(circle 150px at 150px 170px, rgba(190,220,70,0.55), transparent 70%),
      radial-gradient(ellipse 200px 120px at 300px 520px, rgba(170,70,200,0.45), transparent 70%),
      linear-gradient(180deg, #1f3326 0%, #2a2440 55%, #3a2c1e 85%, #241a14 100%);
    -webkit-mask-image: linear-gradient(90deg, #000 70%, transparent 100%);
    mask-image: linear-gradient(90deg, #000 70%, transparent 100%);
  }
  .brand {
    position: absolute;
    left: 770px; top: 62px;
    display: flex; align-items: center; gap: 10px;
    font-family: "Cinzel", serif;
    font-weight: 700;
    font-size: 30px;
    color: var(--logo-blue);
  }
  .brand-mark {
    width: 22px; height: 22px;
    background: var(--logo-blue);
  }
  .title {
    position: absolute;
    left: 515px; top: 118px;
    width: 600px;
    font-family: "Great Vibes", cursive;
    font-size: 98px;
    line-height: 1.2;
    white-space: nowrap;
    color: var(--white);
  }
  .title-accent { color: var(--script-blue); }
  .details-frame {
    position: absolute;
    left: 526px; top: 283px;
    width: 429px; height: 106px;
    border: 3px solid var(--frame);
  }
  .details-banner {
    position: absolute;
    left: 537px; top: 296px;
    width: 405px; height: 81px;
    background: var(--royal);
    display: flex; align-items: center; justify-content: center;
    font-family: "Great Vibes", cursive;
    font-size: 62px;
    color: var(--white);
  }
  .rule {
    position: absolute;
    left: 508px; width: 600px; height: 2px;
    background: linear-gradient(90deg, transparent, var(--rule) 10%, var(--rule) 90%, transparent);
  }
  .label {
    position: absolute;
    left: 537px; width: 127px; height: 42px;
    border: 2px solid var(--frame);
    display: flex; align-items: center; justify-content: center;
    font-family: "Cinzel", serif;
    font-weight: 700;
    font-size: 20px;
    letter-spacing: 2px;
    color: var(--label-blue);
  }
  .value {
    position: absolute;
    left: 698px;
    font-family: "Cinzel", serif;
    font-weight: 400;
    color: var(--white);
    white-space: nowrap;
  }
  .value-date { top: 474px; font-size: 25px; }
  .value-time { top: 562px; font-size: 38px; }
  .value-venue { top: 670px; left: 691px; font-size: 24px; line-height: 27px; }
</style>
</head>
<body>
<main class="invite">
  <div class="venue-photo" role="img" aria-label="Photo of two cocktails on a bar table in a lounge with soft bokeh lights"></div>

  <div class="brand"><span class="brand-mark"></span>PMV</div>

  <h1 class="title"><span class="title-accent">Join us</span> for Dinner</h1>

  <div class="details-frame"></div>
  <h2 class="details-banner">Event Details</h2>

  <div class="rule" style="top:442px"></div>
  <div class="label" style="top:470px">DATE</div>
  <p class="value value-date">TUESDAY, OCTOBER 24TH 2023</p>

  <div class="rule" style="top:538px"></div>
  <div class="label" style="top:565px">TIME</div>
  <p class="value value-time">6:30PM</p>

  <div class="rule" style="top:635px"></div>
  <div class="label" style="top:678px">VENUE</div>
  <p class="value value-venue">VEROLLA CHICAGO, FERN PARLOR<br>347 W HARLOW AVE, CHICAGO, IL 60622</p>
</main>
</body>
</html>
```